Webdesign für Online-Shop für Honig
Zielgruppe
Verkauf von Sidr Honig. Ein sehr hochwertiger Premium-Honig aus dem Jemen.
Aufgabenstellung
Zu Erstellen ist ein Design für einen Onlineshop. Der Onlineshop verkauft Kosmetik-, Lebensmittel- und Gesundheitsprodukte die alle auf einem Honig basieren.
Domain: qalvenu.com
Die Seite soll sehr hochwertig und orientalisch wirken. Der Hintergrund soll auf jeden Fall dunkel sein.
Wir benötigen ein Screendesign der:
- Home-Seite,
- Über uns-Seite
- Produktdetailseite.
Die Designs müssen nicht per HTML umgesetzt werden, können aber. Es reicht ein reines Design als Bild, HTML ist aber auch in Ordnung.
Bitte hochwertige Stockbilder nutzen.

```html
<!DOCTYPE html>
<html lang="en">
<head>
<meta charset="utf-8">
<title>Qalvenu – The Big One</title>
<link rel="stylesheet" href="https://fonts.googleapis.com/css2?family=Cormorant+Garamond:wght@300;400;500&family=Allura&display=swap">
<style>
  :root {
    --bg: #000000;
    --gold: #c48a58;
    --gold-soft: #d6a475;
    --gold-dim: rgba(160, 112, 62, 0.22);
    --photo-top: #e5b98a;
    --photo-bottom: #a27850;
    --dot-dark: #0b0b0b;
  }
  * { margin: 0; padding: 0; box-sizing: border-box; }
  html, body { width: 987px; height: 1200px; overflow: hidden; background: var(--bg); }
  .page {
    position: relative; width: 987px; height: 1200px; overflow: hidden;
    background: var(--bg); color: var(--gold-soft);
    font-family: "Cormorant Garamond", Georgia, serif;
  }
  .pattern { position: absolute; border-radius: 50%; }
  .pattern--left { left: -180px; top: 60px; width: 460px; height: 600px;
    background: radial-gradient(closest-side, var(--gold-dim), rgba(0,0,0,0)); }
  .pattern--right { left: 700px; top: 80px; width: 420px; height: 600px;
    background: radial-gradient(closest-side, var(--gold-dim), rgba(0,0,0,0)); }
  .pattern--footer { left: 200px; top: 900px; width: 600px; height: 420px;
    background: radial-gradient(closest-side, var(--gold-dim), rgba(0,0,0,0)); }

  .brand { position: absolute; display: flex; align-items: center; gap: 8px;
    color: var(--gold); font-weight: 500; letter-spacing: 1px; }
  .brand__mark { width: 12px; height: 12px; border: 1.5px solid var(--gold); border-radius: 50%; }
  .brand--header { left: 78px; top: 66px; font-size: 17px; }
  .tagline { position: absolute; left: 163px; top: 58px; font-family: "Allura", cursive;
    font-size: 22px; color: var(--gold); }
  .tagline { left: 163px; top: 60px; }

  .cart-icon { position: absolute; left: 802px; top: 65px; }
  .menu-icon { position: absolute; left: 850px; top: 69px; }

  .hero-title { position: absolute; left: -4px; top: 176px; font-weight: 300;
    font-size: 74px; line-height: 61px; color: var(--gold); letter-spacing: 1px; }

  .product-info { position: absolute; left: 125px; top: 350px; width: 275px; }
  .product-info__badge { font-family: "Allura", cursive; font-size: 36px; color: var(--gold);
    position: absolute; left: -4px; top: 0; }
  .product-info__name { position: absolute; top: 60px; font-weight: 400; font-size: 29px;
    color: var(--gold); white-space: nowrap; letter-spacing: 0.5px; }
  .product-info__dipper { position: absolute; top: 108px; left: 0; }
  .product-info__text { position: absolute; top: 129px; font-size: 13.5px; line-height: 18.5px;
    color: var(--gold-soft); width: 275px; }
  .product-info__size { position: absolute; top: 219px; font-size: 17px; }
  .product-info__price { position: absolute; top: 256px; font-size: 17px; }
  .add-to-cart { position: absolute; left: 126px; top: 695px; width: 109px; height: 29px;
    border: 1.5px solid var(--gold); color: var(--gold-soft); font-size: 18px;
    display: flex; align-items: center; justify-content: center; }
  .wishlist { position: absolute; left: 264px; top: 701px; }

  .gallery__frame { position: absolute; left: 508px; top: 390px; width: 264px; height: 326px;
    border: 1px solid var(--gold); }
  .gallery__photo { position: absolute; left: 498px; top: 403px; width: 260px; height: 327px;
    background: linear-gradient(180deg, var(--photo-top) 0%, var(--photo-top) 38%, var(--photo-bottom) 100%); }
  .gallery__dots { position: absolute; left: 596px; top: 708px; display: flex; gap: 8px; }
  .gallery__dot { width: 9px; height: 9px; border-radius: 50%; background: var(--dot-dark); }
  .gallery__dot--active { background: var(--photo-top); }
  .gallery__arrow { position: absolute; top: 561px; }
  .gallery__arrow--prev { left: 470px; }
  .gallery__arrow--next { left: 785px; }
  .gallery__caption { position: absolute; left: 662px; top: 706px; font-family: "Allura", cursive;
    font-size: 62px; color: var(--gold); }

  .footer__rule { position: absolute; left: 108px; top: 1006px; width: 770px;
    border-top: 2px dotted var(--gold); }
  .brand--footer { left: 107px; top: 1070px; font-size: 14px; }
  .footer__col { position: absolute; top: 1058px; font-size: 13.5px; line-height: 18.5px;
    color: var(--gold-soft); list-style: none; }
  .footer__col--address { left: 196px; }
  .footer__col--categories { left: 434px; }
  .footer__col--legal { left: 612px; }
  .to-top { position: absolute; left: 904px; top: 1125px; }
</style>
</head>
<body>
<main class="page">
  <div class="pattern pattern--left" role="img" aria-label="Faint oriental ornament pattern"></div>
  <div class="pattern pattern--right" role="img" aria-label="Faint oriental ornament pattern"></div>
  <div class="pattern pattern--footer" role="img" aria-label="Faint oriental ornament pattern"></div>

  <header>
    <div class="brand brand--header"><span class="brand__mark"></span></div>
    <p class="tagline">more than just a honey</p>
    <svg class="cart-icon" width="19" height="24" viewBox="0 0 19 24" fill="none" stroke="#c48a58" stroke-width="1.6">
      <path d="M5 9V5.5a4.5 4.5 0 0 1 9 0V9"/><rect x="1" y="9" width="17" height="14"/>
      <circle cx="9.5" cy="16" r="1.6" fill="#c48a58"/>
    </svg>
    <svg class="menu-icon" width="54" height="18" viewBox="0 0 54 18" stroke="#c48a58" stroke-width="1.6">
      <line x1="6" y1="1" x2="46" y2="1"/><line x1="0" y1="8" x2="54" y2="8"/><line x1="2" y1="16" x2="48" y2="16"/>
    </svg>
  </header>

  <h1 class="hero-title">PREMIUM<br>HONEY</h1>

  <section class="product-info">
    <span class="product-info__badge">new</span>
    <h2 class="product-info__name">THE BIG ONE</h2>
    <svg class="product-info__dipper" width="20" height="16" viewBox="0 0 20 16" fill="none" stroke="#c48a58" stroke-width="1.4">
      <line x1="0" y1="1" x2="11" y2="6"/><ellipse cx="14" cy="9" rx="4" ry="3.5" transform="rotate(30 14 9)"/>
    </svg>
    <p class="product-info__text">Ut wisi enim ad minim veniam, tion ullamcorper suscipit lob.Lorem ipsum dolor sit amet, consectetuer adipiscing elit, sed diam nonummy nibh euismod tincidunt ut laoreet dolore.</p>
    <p class="product-info__size">1 kg</p>
    <p class="product-info__price">€ 60,-</p>
  </section>
  <a class="add-to-cart">add to cart</a>
  <svg class="wishlist" width="21" height="19" viewBox="0 0 21 19" fill="none" stroke="#c48a58" stroke-width="1.3">
    <path d="M10.5 18 2 9.5A4.8 4.8 0 0 1 10.5 3a4.8 4.8 0 0 1 8.5 6.5Z"/>
  </svg>

  <section class="gallery">
    <div class="gallery__frame"></div>
    <div class="gallery__photo" role="img" aria-label="Product photo: dark glass honey jar on a warm amber background"></div>
    <div class="gallery__dots">
      <span class="gallery__dot gallery__dot--active"></span><span class="gallery__dot"></span><span class="gallery__dot"></span>
    </div>
    <svg class="gallery__arrow gallery__arrow--prev" width="14" height="28" viewBox="0 0 14 28" fill="none" stroke="#c48a58" stroke-width="1.4"><polyline points="13,1 1,14 13,27"/></svg>
    <svg class="gallery__arrow gallery__arrow--next" width="14" height="28" viewBox="0 0 14 28" fill="none" stroke="#c48a58" stroke-width="1.4"><polyline points="1,1 13,14 1,27"/></svg>
    <span class="gallery__caption">tasty</span>
  </section>

  <footer>
    <div class="footer__rule"></div>
    <div class="brand brand--footer"><span class="brand__mark"></span></div>
    <ul class="footer__col footer__col--address">
      <li>QALVENU PREMIUM HONEY</li><li>Street Number 123</li><li>1234 City</li>
    </ul>
    <ul class="footer__col footer__col--categories">
      <li>Healthy</li><li>Beauty</li><li>Tasty</li>
    </ul>
    <ul class="footer__col footer__col--legal">
      <li>Impressum</li><li>AGB</li>
    </ul>
    <svg class="to-top" width="48" height="48" viewBox="0 0 48 48" fill="none" stroke="#c48a58" stroke-width="1.3">
      <circle cx="24" cy="24" r="23"/><polyline points="12,29 24,17 36,29"/>
    </svg>
  </footer>
</main>
</body>
</html>
```